Real Estate Search Site Re-Design of 2 Pages

Looking for designs to optimize 2 pages of our current site design. Our site allows users to find properties to purchase or rent.

Basically there are 4 panes
1. The top red one where you actually type in what you''re looking for.
2. The map pane that shows the properties
3. The scrollable results pane.
4. Property details pane.

A typical search would go like this:
1. User fills in their search criteria in the top pane in red. Clicks Find Homes
2. Site updates the map with properties plotted that fit the criteria. Site also populates the results pane at the bottom. Site shows the most newest property that fits the search criteria on the right.
3. User will scroll through the results pane or the map and click a property.
4. Site will update the property details pane with information on the selected property.

Search/Results Page
This main page needs a search form area, a results area, an area to display details of a property selected, a map to show results, and an area to display a real estate agent's information. The design must be full-screen to use all the space on the screen. All information should fit on a 1366x768 screen size. Please see sample screen shot.

Property Details Page
This one can be fixed width of 978px. This page needs all the elements that are displayed in the sample PNG file. Ideally, we want to be able to see all important information without scrolling on a 1366x768 screen. The important information in this size are Pictures with controls, address, bedrooms, bathrooms, square feet, square feet of the lot, days on market, agent information, and buttons to request a showing or get more information.

Our Goal:
Our goal is to get create a different way to display the data in an effective way. We want different ways to show the search results, maybe a vertical, scrolling list of property information with pictures. Or even a horizontal scrolling results pane. It must contain:

1. A map of the results
2. A way to scroll through the search results (like we have currently in case someone wants to search/sort bedrooms or square footage)
3. A way to view details of the property
4. A way to display agent information/picture

There's a lot of good design work coming through. Thank you.

Perhaps review some other real estate sales sites for ideas on pane configuration. Example site links:
http://www.brovenly.com/homes/for_sale/?gclid=QmTr8k2-xw7HJd3P9Lq0VnE5ZB (brovenly.com)
http://www.pemoda.com/?sem=1.2.1.5.7.1.0.14&gclid=ZKwp42h-ty8NGRmX5BqeuLcHTD (Pemoda.com)
http://www.quivrent.com/map_search/results/i/ (quivrent.com)

Our goal for the redesign is to display the data in a more effective way. Either with a better flow, more pictures, more information, smoother search process. Please see the updated brief for details. The main idea is to show the data in the most effective way possible.

Project Deadline Extended
Reason: Still looking at different ideas for the search results. We are still open for fresh ideas.

Industry/Entity Type

Real Estate

Font styles to use
Sans Serif

Colors
eb1f27

```html
<!DOCTYPE html>
<html lang="en">
<head>
<meta charset="utf-8">
<title>Home Search Results</title>
<link href="https://fonts.googleapis.com/css2?family=Open+Sans:wght@400;600;700&display=swap" rel="stylesheet">
<style>
:root{
  --red:#b70d10;
  --red-dark:#9c0708;
  --accent:#e0141b;
  --orange:#f0622a;
  --orange-text:#f25a1e;
  --text:#333;
  --muted:#666;
  --line:#dcdcdc;
  --panel:#f6f6f6;
  --footer:#3a3a3a;
}
*{box-sizing:border-box;margin:0;padding:0}
html,body{width:833px;height:1200px;overflow:hidden;background:#fff;font-family:"Open Sans",Arial,sans-serif;color:var(--text)}
.page{position:relative;width:833px;height:1200px}

/* header */
.site-header{position:absolute;left:0;top:0;width:833px;height:76px;background:linear-gradient(#c4100f,var(--red-dark))}
.brand{position:absolute;left:28px;top:28px;display:flex;align-items:center;gap:6px;color:#fff;font-weight:700;font-size:18px}
.brand-mark{width:22px;height:22px;background:#fff;display:inline-block}
.field-label{position:absolute;color:#fff;font-size:9px}
.input{position:absolute;height:17px;background:#fff;border:1px solid #ccc;border-radius:3px;font-size:7.5px;color:#777;padding:3px 6px;line-height:10px}
.select{position:absolute;height:16px;border:1px solid #e6a0a0;border-radius:2px;background:#c8211f;font-size:7.5px;color:#f3d0d0;padding:2px 5px;line-height:11px}
.select::after{content:"";position:absolute;right:5px;top:6px;border:3px solid transparent;border-top-color:#f3d0d0}
.find-btn{position:absolute;left:289px;top:10px;width:81px;height:18px;background:linear-gradient(#f7903f,#ea6a1a);border-radius:3px;color:#fff;font-size:7.5px;text-align:center;line-height:18px}
.lang{position:absolute;left:665px;top:14px;color:#fff;font-size:9px}
.flag{position:absolute;top:13px;width:17px;height:11px;border:1px solid #fff}
.main-nav{position:absolute;top:51px;color:#fff;font-size:8.5px;font-weight:600}

/* map */
.map{position:absolute;left:0;top:76px;width:833px;height:298px;background:linear-gradient(135deg,#f1eee6,#e6e8dc 50%,#eceadf);border-bottom:3px solid var(--accent);overflow:hidden}
.pin{position:absolute;width:26px;height:34px}
.zoom{position:absolute;left:799px;top:216px;width:18px;height:54px;background:#fff;border:1px solid #ccc;font-size:11px;color:#666;text-align:center;line-height:17px}

/* popup */
.popup{position:absolute;left:534px;top:112px;width:189px;height:224px;background:#fff;box-shadow:0 0 4px rgba(0,0,0,.3);padding:8px 13px}
.popup-title{color:var(--accent);font-size:8px;font-weight:600;line-height:14px}
.popup-photo{margin-top:7px;width:161px;height:86px;background:linear-gradient(#8fb2d6,#c7ccd1 55%,#6a7a4a);position:relative}
.photo-bar{position:absolute;left:0;bottom:0;width:100%;height:14px;background:rgba(0,0,0,.55);color:#fff;font-size:7px;text-align:center;line-height:14px}
.photo-bar span{position:absolute;top:0}
.popup-row{font-size:7px;color:#444;margin-top:6px;white-space:nowrap}
.popup-row b{font-weight:600;color:#222}
.popup-btn{position:absolute;top:195px;width:68px;height:22px;background:var(--accent);color:#fff;font-size:7px;text-align:center;line-height:22px;border-radius:3px}

/* listing cards */
.card{position:absolute;width:137px;height:163px;border:1px solid var(--line);background:#fff;text-align:center}
.card-addr{font-size:7.5px;color:#555;margin-top:9px}
.card-city{font-size:9.5px;font-weight:600;color:#222;margin-top:2px}
.card-age{font-size:7px;color:var(--orange-text);margin-top:4px}
.card-photo{position:absolute;left:0;top:55px;width:135px;height:93px}
.tone-a{background:linear-gradient(#d6d0c5,#a79a82 55%,#5b6b3c)}
.tone-b{background:linear-gradient(#aac7e4,#cfc4b2 55%,#6f8a46)}
.tone-c{background:linear-gradient(#bccbd6,#8f8675 55%,#58653c)}
.card-price{position:absolute;left:0;top:8px;width:100%;color:var(--accent);font-weight:700;font-size:10px}
.card-stats{position:absolute;left:0;bottom:0;width:100%;height:13px;background:rgba(255,255,255,.75);display:flex}
.card-stats span,.card-labels span{flex:1;font-size:8px;font-weight:600;color:#222;line-height:13px}
.card-labels{position:absolute;left:0;top:148px;width:100%;height:15px;display:flex}
.card-labels span{font-size:6.5px;font-weight:400;color:#555;line-height:15px;border-right:1px solid var(--line)}
.card-labels span:last-child{border-right:0}

/* agents */
.agents-head{position:absolute;left:572px;top:412px;width:135px;height:30px;background:var(--accent);color:#fff;font-weight:600;font-size:11px;padding-left:10px;line-height:30px}
.agent{position:absolute;left:572px;width:135px;height:168px;background:var(--panel);border:1px solid var(--line);text-align:center}
.avatar{width:64px;height:64px;border-radius:50%;margin:12px auto 0;background:linear-gradient(#7d8a96,#c9b6a5)}
.agent-name{font-size:8.5px;font-weight:600;margin-top:10px;color:#222}
.agent-line{font-size:8px;color:#444;margin-top:8px;display:flex;justify-content:center;align-items:center;gap:4px}
.agent-mail{color:var(--orange-text)}
.view-all{position:absolute;left:586px;top:1010px;width:106px;height:32px;background:var(--orange);color:#fff;font-size:10.5px;font-weight:600;text-align:center;line-height:32px}

.site-footer{position:absolute;left:0;top:1147px;width:833px;height:53px;background:var(--footer);color:#eee;font-size:8px;text-align:center;line-height:50px}
</style>
</head>
<body>
<div class="page">

<header class="site-header">
  <div class="brand"><span class="brand-mark"></span>LOGO</div>
  <span class="field-label" style="left:126px;top:14px">Location</span>
  <div class="input" style="left:164px;top:10px;width:116px">Alhambra</div>
  <div class="find-btn">&#9906; FIND HOMES</div>
  <span class="lang">Language :</span>
  <span class="flag" style="left:716px;background:#223f8a"></span>
  <span class="flag" style="left:741px;background:#d81e1e"></span>
  <span class="flag" style="left:765px;background:#3a4f9a"></span>

  <span class="field-label" style="left:138px;top:51px">Type</span>
  <div class="select" style="left:163px;top:48px;width:116px">Condo/Townhouse</div>
  <span class="field-label" style="left:291px;top:51px">Price</span>
  <div class="select" style="left:317px;top:48px;width:49px">$500k</div>
  <span class="field-label" style="left:373px;top:51px">to</span>
  <div class="select" style="left:389px;top:48px;width:45px">$1M</div>
  <span class="field-label" style="left:446px;top:51px">Beds</span>
  <div class="select" style="left:472px;top:48px;width:30px">3+</div>
  <span class="field-label" style="left:518px;top:51px">Baths</span>
  <div class="select" style="left:549px;top:48px;width:30px">2+</div>

  <nav>
    <span class="main-nav" style="left:610px">COMMUNITIES</span>
    <span class="main-nav" style="left:688px">LOCATIONS</span>
    <span class="main-nav" style="left:754px">CONTACT</span>
  </nav>
</header>

<section class="map" role="img" aria-label="Road map of the search area with property markers">
  <svg width="0" height="0" style="position:absolute"><defs>
    <symbol id="pin" viewBox="0 0 26 34"><path d="M13 33C13 33 1 19 1 12.5A12 12 0 0 1 25 12.5C25 19 13 33 13 33Z" fill="#e0141b" stroke="#fff" stroke-width="1.5"/><path d="M7 14l6-5 6 5v5h-12z" fill="#fff"/></symbol>
  </defs></svg>
  <svg class="pin" style="left:187px;top:61px"><use href="#pin"/></svg>
  <svg class="pin" style="left:333px;top:57px"><use href="#pin"/></svg>
  <svg class="pin" style="left:493px;top:82px"><use href="#pin"/></svg>
  <svg class="pin" style="left:327px;top:130px"><use href="#pin"/></svg>
  <svg class="pin" style="left:83px;top:211px"><use href="#pin"/></svg>
  <svg class="pin" style="left:345px;top:236px"><use href="#pin"/></svg>
  <svg class="pin" style="left:503px;top:190px"><use href="#pin"/></svg>
  <svg class="pin" style="left:761px;top:63px"><use href="#pin"/></svg>
  <div class="zoom">&#9679;<br>+<br>&minus;</div>
</section>

<aside class="popup">
  <div class="popup-title">2418 Verano Crest Drive Maple Hollow</div>
  <div class="popup-photo" role="img" aria-label="Photo of a large two-storey white house">
    <div class="photo-bar"><span style="left:8px">&lsaquo;</span>1/32<span style="right:8px">&rsaquo;</span></div>
  </div>
  <div class="popup-row" style="margin-top:12px">Listing Price &nbsp;: &nbsp;<b>$2,388,000</b></div>
  <div class="popup-row">Beds &nbsp;: &nbsp;3 &nbsp;&nbsp;&nbsp;&nbsp; Baths &nbsp;: &nbsp;3 &nbsp;&nbsp;&nbsp;&nbsp; Built in : 2014</div>
  <div class="popup-row">3,640 Sq. Ft ($656/Sq.Ft.) &nbsp;<span style="color:var(--orange-text)">25 Days on Market</span></div>
  <div class="popup-btn" style="left:12px">VIEW DETAILS</div>
  <div class="popup-btn" style="left:92px">VISIT HOME</div>
</aside>

<main>
<article class="card" style="left:125px;top:412px"><div class="card-addr">2418 Verano Crest Drive</div><div class="card-city">Maple Hollow</div><div class="card-age">5 Days ago</div>
<div class="card-photo tone-a" role="img" aria-label="Photo of a house at dusk"><div class="card-price">$1,200,000</div><div class="card-stats"><span>4</span><span>2.5</span><span>1,814</span><span>$765</span></div></div>
<div class="card-labels"><span>Beds</span><span>Baths</span><span>Sq. Ft.</span><span>$/Sq. Ft</span></div></article>
<article class="card" style="left:274px;top:412px"><div class="card-addr">2418 Verano Crest Drive</div><div class="card-city">Maple Hollow</div><div class="card-age">5 Days ago</div>
<div class="card-photo tone-b" role="img" aria-label="Photo of a stucco house"><div class="card-price">$1,200,000</div><div class="card-stats"><span>4</span><span>2.5</span><span>1,814</span><span>$765</span></div></div>
<div class="card-labels"><span>Beds</span><span>Baths</span><span>Sq. Ft.</span><span>$/Sq. Ft</span></div></article>
<article class="card" style="left:422px;top:412px"><div class="card-addr">2418 Verano Crest Drive</div><div class="card-city">Maple Hollow</div><div class="card-age">5 Days ago</div>
<div class="card-photo tone-c" role="img" aria-label="Photo of a stone house"><div class="card-price">$1,200,000</div><div class="card-stats"><span>4</span><span>2.5</span><span>1,814</span><span>$765</span></div></div>
<div class="card-labels"><span>Beds</span><span>Baths</span><span>Sq. Ft.</span><span>$/Sq. Ft</span></div></article>

<article class="card" style="left:125px;top:590px"><div class="card-addr">2418 Verano Crest Drive</div><div class="card-city">Maple Hollow</div><div class="card-age">5 Days ago</div>
<div class="card-photo tone-a" role="img" aria-label="Photo of a modern house"><div class="card-price">$1,200,000</div><div class="card-stats"><span>4</span><span>2.5</span><span>1,814</span><span>$765</span></div></div>
<div class="card-labels"><span>Beds</span><span>Baths</span><span>Sq. Ft.</span><span>$/Sq. Ft</span></div></article>
<article class="card" style="left:274px;top:590px"><div class="card-addr">2418 Verano Crest Drive</div><div class="card-city">Maple Hollow</div><div class="card-age">5 Days ago</div>
<div class="card-photo tone-b" role="img" aria-label="Photo of a grey colonial house"><div class="card-price">$1,200,000</div><div class="card-stats"><span>4</span><span>2.5</span><span>1,814</span><span>$765</span></div></div>
<div class="card-labels"><span>Beds</span><span>Baths</span><span>Sq. Ft.</span><span>$/Sq. Ft</span></div></article>
<article class="card" style="left:422px;top:590px"><div class="card-addr">2418 Verano Crest Drive</div><div class="card-city">Maple Hollow</div><div class="card-age">5 Days ago</div>
<div class="card-photo tone-c" role="img" aria-label="Photo of a house with porch"><div class="card-price">$1,200,000</div><div class="card-stats"><span>4</span><span>2.5</span><span>1,814</span><span>$765</span></div></div>
<div class="card-labels"><span>Beds</span><span>Baths</span><span>Sq. Ft.</span><span>$/Sq. Ft</span></div></article>

<article class="card" style="left:125px;top:769px"><div class="card-addr">2418 Verano Crest Drive</div><div class="card-city">Maple Hollow</div><div class="card-age">5 Days ago</div>
<div class="card-photo tone-c" role="img" aria-label="Photo of a house with trees"><div class="card-price">$1,200,000</div><div class="card-stats"><span>4</span><span>2.5</span><span>1,814</span><span>$765</span></div></div>
<div class="card-labels"><span>Beds</span><span>Baths</span><span>Sq. Ft.</span><span>$/Sq. Ft</span></div></article>
<article class="card" style="left:274px;top:769px"><div class="card-addr">2418 Verano Crest Drive</div><div class="card-city">Maple Hollow</div><div class="card-age">5 Days ago</div>
<div class="card-photo tone-a" role="img" aria-label="Photo of a dark two-storey house"><div class="card-price">$1,200,000</div><div class="card-stats"><span>4</span><span>2.5</span><span>1,814</span><span>$765</span></div></div>
<div class="card-labels"><span>Beds</span><span>Baths</span><span>Sq. Ft.</span><span>$/Sq. Ft</span></div></article>
<article class="card" style="left:422px;top:769px"><div class="card-addr">2418 Verano Crest Drive</div><div class="card-city">Maple Hollow</div><div class="card-age">5 Days ago</div>
<div class="card-photo tone-b" role="img" aria-label="Photo of a timber-clad house"><div class="card-price">$1,200,000</div><div class="card-stats"><span>4</span><span>2.5</span><span>1,814</span><span>$765</span></div></div>
<div class="card-labels"><span>Beds</span><span>Baths</span><span>Sq. Ft.</span><span>$/Sq. Ft</span></div></article>

<article class="card" style="left:125px;top:947px"><div class="card-addr">2418 Verano Crest Drive</div><div class="card-city">Maple Hollow</div><div class="card-age">5 Days ago</div>
<div class="card-photo tone-a" role="img" aria-label="Photo of a brick house with garage"><div class="card-price">$1,200,000</div><div class="card-stats"><span>4</span><span>2.5</span><span>1,814</span><span>$765</span></div></div>
<div class="card-labels"><span>Beds</span><span>Baths</span><span>Sq. Ft.</span><span>$/Sq. Ft</span></div></article>
<article class="card" style="left:274px;top:947px"><div class="card-addr">2418 Verano Crest Drive</div><div class="card-city">Maple Hollow</div><div class="card-age">5 Days ago</div>
<div class="card-photo tone-c" role="img" aria-label="Photo of a stone-front house"><div class="card-price">$1,200,000</div><div class="card-stats"><span>4</span><span>2.5</span><span>1,814</span><span>$765</span></div></div>
<div class="card-labels"><span>Beds</span><span>Baths</span><span>Sq. Ft.</span><span>$/Sq. Ft</span></div></article>
<article class="card" style="left:422px;top:947px"><div class="card-addr">2418 Verano Crest Drive</div><div class="card-city">Maple Hollow</div><div class="card-age">5 Days ago</div>
<div class="card-photo tone-b" role="img" aria-label="Photo of a family house with lawn"><div class="card-price">$1,200,000</div><div class="card-stats"><span>4</span><span>2.5</span><span>1,814</span><span>$765</span></div></div>
<div class="card-labels"><span>Beds</span><span>Baths</span><span>Sq. Ft.</span><span>$/Sq. Ft</span></div></article>
</main>

<aside>
  <svg width="0" height="0" style="position:absolute"><defs>
    <symbol id="phone" viewBox="0 0 8 11"><rect x="1" y="0.5" width="6" height="10" rx="1" fill="none" stroke="#666"/><rect x="2.5" y="2" width="3" height="5" fill="#666"/></symbol>
    <symbol id="mail" viewBox="0 0 13 9"><rect width="13" height="9" fill="#f25a1e"/><path d="M0 0l6.5 5L13 0M0 9l5-4.5M13 9l-5-4.5" stroke="#fff" fill="none"/></symbol>
  </defs></svg>
  <div class="agents-head">Buyer's Agent</div>
  <div class="agent" style="top:455px">
    <div class="avatar" role="img" aria-label="Agent portrait"></div>
    <div class="agent-name">Lena Harlow</div>
    <div class="agent-line"><svg width="8" height="11"><use href="#phone"/></svg>- (555) 014-2287</div>
    <div class="agent-line agent-mail"><svg width="13" height="9"><use href="#mail"/></svg>lena@homeroost.com</div>
    <div class="agent-line">BRE #04812935</div>
  </div>
  <div class="agent" style="top:639px">
    <div class="avatar" role="img" aria-label="Agent portrait"></div>
    <div class="agent-name">Lena Harlow</div>
    <div class="agent-line"><svg width="8" height="11"><use href="#phone"/></svg>- (555) 014-2287</div>
    <div class="agent-line agent-mail"><svg width="13" height="9"><use href="#mail"/></svg>lena@homeroost.com</div>
    <div class="agent-line">BRE #04812935</div>
  </div>
  <div class="agent" style="top:826px">
    <div class="avatar" role="img" aria-label="Agent portrait"></div>
    <div class="agent-name">Lena Harlow</div>
    <div class="agent-line"><svg width="8" height="11"><use href="#phone"/></svg>- (555) 014-2287</div>
    <div class="agent-line agent-mail"><svg width="13" height="9"><use href="#mail"/></svg>lena@homeroost.com</div>
    <div class="agent-line">BRE #04812935</div>
  </div>
  <div class="view-all">View All</div>
</aside>

<footer class="site-footer">Copyright @ 2014 Domain Name. All right reserved.</footer>
</div>
</body>
</html>
```